Book Cover Design on Conflict resolution

I need a book cover design for the following book title. Title: "The Quiet Bridge: Steering Disputes with Candor, Social Awareness, and Steady Grit" The author's name is Marcus Dravel. The book covers multiple areas to include unconscious bias, retaliation and reprisal. I am interested in seeing the designs that provide a unique eye catching presence.

Target Market(s)

Organizations and major corporations. Personal conflicts and self help. Federal Government, Schools, and Churches

Industry/Entity Type

Large Corporation, Federal Government, Churches, Schools

Font styles to use
Serif

Colors
0054AA
0677BA
7BADD7
CADEEF
E8F1F8
59FF00
82FF00
B8FF75
E3FFCB
F4FFEA

Requirements
Nice to have
• something unique and creative

```html
<!DOCTYPE html>
<html lang="en">
<head>
<meta charset="utf-8">
<title>The Quiet Bridge — Marcus Dravel</title>
<link rel="stylesheet" href="https://fonts.googleapis.com/css2?family=DM+Serif+Display&family=Lora:wght@400;700&display=swap">
<style>
  :root {
    --backdrop: #6f6f6f;
    --cover: #e8f1f8;
    --ink: #0c1b2e;
    --dot-navy: #0054aa;
    --dot-sky: #0677ba;
    --dot-lime: #59ff00;
  }
  * { box-sizing: border-box; margin: 0; padding: 0; }
  html, body {
    width: 1200px;
    height: 720px;
    overflow: hidden;
    background: var(--backdrop);
  }
  .canvas {
    position: relative;
    width: 1200px;
    height: 720px;
    display: flex;
    align-items: center;
    justify-content: center;
  }
  .cover {
    position: relative;
    width: 510px;
    height: 650px;
    background: var(--cover);
    color: var(--ink);
  }
  .title {
    position: absolute;
    left: 48px;
    top: 56px;
    font-family: "DM Serif Display", serif;
    font-weight: 400;
    font-size: 118px;
    line-height: 100px;
    letter-spacing: 1px;
    text-transform: lowercase;
  }
  .title-line { display: block; white-space: nowrap; }
  .dot {
    display: inline-block;
    width: 0.5em;
    height: 0.5em;
    border-radius: 50%;
    vertical-align: baseline;
    margin: 0 0.03em;
  }
  .dot--navy { background: var(--dot-navy); }
  .dot--sky { background: var(--dot-sky); }
  .dot--lime { background: var(--dot-lime); }
  .lead-in {
    position: absolute;
    left: 40px;
    top: 408px;
    display: flex;
    align-items: flex-start;
    gap: 32px;
  }
  .lead-in .dot { font-size: 118px; margin: 0; flex: none; }
  .subtitle {
    font-family: "Lora", serif;
    font-weight: 400;
    font-size: 14px;
    line-height: 18px;
    padding-top: 4px;
  }
  .author {
    position: absolute;
    left: 0;
    right: 0;
    bottom: 76px;
    text-align: center;
    font-family: "Lora", serif;
    font-weight: 700;
    font-size: 22px;
    letter-spacing: 0.5px;
    text-transform: uppercase;
  }
</style>
</head>
<body>
  <main class="canvas">
    <section class="cover">
      <h1 class="title" aria-label="The Quiet Bridge">
        <span class="title-line">th<span class="dot dot--navy"></span></span>
        <span class="title-line">qui<span class="dot dot--sky"></span>t</span>
        <span class="title-line">bridg</span>
      </h1>
      <div class="lead-in">
        <span class="dot dot--lime"></span>
        <p class="subtitle">Steering Disputes with<br>Candor,<br>Social Awareness, and<br>Steady Grit</p>
      </div>
      <p class="author">Marcus Dravel</p>
    </section>
  </main>
</body>
</html>
```